Tovix Template KFZ-Teile und Zubehör
Zielgruppe
professionell wirkendes Template, welches den Hobbyschrauber, aber auch KFZ-Werkstätten anspricht.
Hallo liebe Designer,
wir sind ein Online-Unternehmen, welches KFZ-Teile & -Zubehör vertreibt.
Um unseren Tovix-Shop neu zu gestalten, suchen wir aktuell nach einem geeigneten Template. Wir nutzen JTL Wawi. Das Template sollte gemäß Anhang aufgebaut sein, sodass wir es problemlos importieren können. Im Header muss unser Logo erscheinen.

```html
<!DOCTYPE html>
<html lang="de">
<head>
<meta charset="utf-8">
<title>Kolbenwerk Teile – Tovix-Shop Template</title>
<link href="https://fonts.googleapis.com/css2?family=Open+Sans:wght@400;600;700&family=Roboto:wght@300;400&display=swap" rel="stylesheet">
<style>
:root{
  --red:#c8001a;
  --ink:#222;
  --text:#333;
  --muted:#555;
  --rule:#d8d8d8;
  --panel:#efefef;
  --tab-top:#fafafa;
  --tab-bottom:#dcdcdc;
  --fold:#a8a8a8;
}
*{box-sizing:border-box;margin:0;padding:0}
html,body{width:1095px;height:1200px;overflow:hidden;background:#fff}
body{position:relative;font-family:Arial,Helvetica,sans-serif;color:var(--text)}
.frame-line{position:absolute;left:138px;top:156px;width:1px;height:1044px;background:#e2e2e2}
.header-line{position:absolute;left:138px;top:155px;width:940px;height:1px;background:#e6e6e6}

.brand{position:absolute;left:146px;top:60px;display:flex;align-items:center;gap:10px}
.brand-mark{width:40px;height:40px;border-radius:50%;background:var(--red)}
.brand-text{display:flex;flex-direction:column;font-family:'Open Sans',sans-serif}
.brand-name{font-size:26px;font-weight:700;color:var(--red);letter-spacing:.5px;line-height:1}
.brand-url{font-size:12px;color:var(--ink);margin-top:6px}

.nav{position:absolute;display:flex;font-family:'Open Sans',sans-serif;font-weight:700;font-size:8.6px;color:var(--ink)}
.nav a{color:inherit;text-decoration:none;padding:0 6px;border-left:1.5px solid var(--red);line-height:13px}
.nav a:first-child{border-left:none;padding-left:0}
.nav-top{left:400px;top:116px}
.nav-foot{left:375px;top:1157px}

.tab{position:absolute;left:121px;height:37px;padding:0 14px 0 26px;display:flex;align-items:center;
  font-family:'Open Sans',sans-serif;font-weight:600;font-size:16px;color:var(--ink);
  background:linear-gradient(var(--tab-top),var(--tab-bottom));box-shadow:1px 2px 3px rgba(0,0,0,.25)}
.tab::after{content:"";position:absolute;left:0;top:37px;border-top:7px solid var(--fold);border-left:17px solid transparent}

.product-photo{position:absolute;left:262px;top:196px;width:118px;height:96px;border-radius:10px;
  background:radial-gradient(circle at 35% 50%,#e9a06b 0,#d9602e 45%,#c2381e 75%,#fff 100%)}
.photo-shadow{position:absolute;left:248px;top:294px;width:132px;height:3px;background:linear-gradient(90deg,transparent,#333 20%,#333 80%,transparent)}
.caption{position:absolute;left:196px;top:317px;font-family:'Roboto',sans-serif;font-weight:300;font-size:12.6px;color:var(--ink)}

.description{position:absolute;left:495px;top:156px;width:400px;height:204px;background:linear-gradient(90deg,#f2f2f2,#ececec);padding:18px 16px}
.description h2{font-family:'Open Sans',sans-serif;font-weight:700;font-size:15.5px;color:var(--red);margin-bottom:12px}
.description p{font-family:'Roboto',sans-serif;font-weight:300;font-size:12.6px;color:var(--ink);line-height:15.5px}
.description .title{margin-bottom:14px}

.divider{position:absolute;left:145px;width:750px;height:0;border-top:2px dotted var(--rule)}

.copy{position:absolute;left:160px;width:735px;font-size:8.3px;line-height:11.2px;color:var(--text)}
.copy ul{list-style:none;margin-top:0}
.copy li{position:relative;padding-left:15px}
.copy li::before{content:"";position:absolute;left:4px;top:3.5px;width:4px;height:4px;border-radius:50%;background:#111}
.gap{margin-top:11px}
</style>
</head>
<body>
<div class="header-line"></div>
<div class="frame-line"></div>

<header>
  <div class="brand">
    <span class="brand-mark"></span>
    <div class="brand-text">
      <span class="brand-name">KOLBENWERK</span>
      <span class="brand-url">www.kolbenwerk-teile.de</span>
    </div>
  </div>
  <nav class="nav nav-top">
    <a href="#">Tovix-Shop</a><a href="#">Unsere Bewertungen</a><a href="#">Weitere Auktionen</a><a href="#">Versand</a><a href="#">Zahlung</a><a href="#">Kaufabwicklung</a>
  </nav>
</header>

<section>
  <div class="tab" style="top:182px">Bilder</div>
  <div class="product-photo" role="img" aria-label="Produktfoto: zwei orange Rundluftfilter"></div>
  <div class="photo-shadow"></div>
  <p class="caption">Klicken Sie auf ein Bild, um es zu vergrößern</p>
  <div class="description">
    <h2>Produktbeschreibung</h2>
    <p class="title">LUFTFILTER CITYCAR</p>
    <p>Höhe 135mm<br>Außendurchmesser 92mm<br>Innendurchmesser 49mm</p>
  </div>
  <div class="divider" style="top:364px"></div>
</section>

<section>
  <div class="tab" style="top:392px">Zahlung</div>
  <div class="copy" style="top:448px">
    <p>Lorem ipsum dolor sit etconsectetur adipisicing elit, sed do eiusmod tempor incididunt ut labore et dolore magna aliqua.Lorem ipsum dolor sit etconsectetur adipisicing elit, sed do eiusmod tempor incididunt ut labore et dolore magna aliqua.Lorem ipsum dolor sit etconsectetur adipisicing elit, sed do eiusmod tempor incididunt ut labore et dolore magna aliqua. Bitte warten Sie nach dem Kauf auf unsere E-Mail, welche sämtliche Zahlungsinformationen enthält.</p>
    <p class="gap">Wir akzeptieren folgende Zahlungsweise:</p>
    <ul>
      <li>Online-Wallet</li>
      <li>Vorkasse</li>
      <li>Überweisung</li>
      <li>Barzahlung bei Abholung (kurzfristig Termin vereinbaren)</li>
    </ul>
  </div>
  <div class="divider" style="top:572px"></div>
</section>

<section>
  <div class="tab" style="top:599px">Kaufabwicklung</div>
  <div class="copy" style="top:656px">
    <p>Sie erhalten automatisch nach der Auktion an Ihre bei Tovix hinterlegte E-Mailadresse eine E-Mail zur Einleitung der Kaufabwicklung. In der Kaufabwicklung können Sie mehrere Auktionen von uns zusammenfassen und Versandkosten sparen, Ihre Rechnungs- und Lieferadresse anpassen sowie die Zahlungsart und Versandart wählen. Ebenso finden Sie dort alle Informationen zur Zahlungsabwicklung wie etwa unsere Kontodaten und Verwendungszweck im Falle der Zahlungsart Vorauskasse / Überweisung. Sollten Sie diese E-Mail innerhalb von 2 Stunden nicht erhalten, so nehmen Sie bitte Kontakt mit uns auf.</p>
  </div>
  <div class="divider" style="top:716px"></div>
</section>

<section>
  <div class="tab" style="top:744px">Versand</div>
  <div class="copy" style="top:800px">
    <p>Lorem ipsum dolor sit etconsectetur adipisicing elit, sed do eiusmod tempor incididunt ut labore et dolore magna aliqua.Lorem ipsum dolor sit etconsectetur adipisicing elit, sed do eiusmod tempor incididunt ut labore et dolore magna aliqua.Lorem ipsum dolor sit etconsectetur adipisicing elit, sed do eiusmod tempor incididunt ut labore et dolore magna aliqua.Lorem ipsum dolor sit etconsectetur adipisicing elit, sed do eiusmod tempor incididunt ut labore et dolore magna aliqua.Lorem ipsum dolor sit etconsectetur adipisicing elit, sed do eiusmod tempor incididunt ut labore et dolore magna aliqua.Lorem ipsum dolor sit etconsectetur adipisicing elit, sed do eiusmod tempor incididunt ut labore et dolore magna aliqua.Lorem ipsum dolor sit etconsectetur adipisicing elit, sed do eiusmod tempor incididunt ut labore et dolore magna aliqua.Lorem ipsum dolor sit etconsectetur adipisicing elit, sed do eiusmod tempor incididunt ut labore et dolore magna aliqua.</p>
  </div>
  <div class="divider" style="top:872px"></div>
</section>

<section>
  <div class="tab" style="top:900px">Rückgaberecht</div>
  <div class="copy" style="top:956px">
    <p>Widerrufsbelehrung Widerrufsrecht Sie können Ihre Vertragserklärung innerhalb von 14 Tagen ohne Angabe von Gründen in Text-form (z.B. Brief, Fax, E-Mail) oder - wenn Ihnen die Sache vor Fristablauf überlassen wird - auch durch Rücksendung der Sache widerrufen. Die Frist beginnt nach Erhalt dieser Belehrung in Textform, jedoch nicht vor Eingang der Ware beim Empfänger (bei der wiederkehrenden Liefe-rung gleichartiger Waren nicht vor Eingang der ersten Teillieferung) und auch nicht vor Erfüllung unserer Informationspflichten gemäß Artikel 246 § 2 in Verbindung mit § 1 Absatz 1 und 2 EGBGB sowie unserer Pflichten gemäß § 312g Absatz 1 Satz 1 BGB in Verbindung mit Artikel 246 § 3 EGBGB. Zur Wahrung der Widerrufsfrist genügt die rechtzeitige Absendung des Widerrufs oder der Sache. Der Widerruf ist zu richten an: Konrad Weller, Kolbenwerk Teile Lindenstr. 42 04109 Leipzig shop@kolbenwerk-teile.de Fax: 0341 555 01 23 Widerrufsfolgen Im Falle eines wirksamen Widerrufs sind die beiderseits empfangenen Leistungen zurückzuge-währen und ggf. gezogene Nutzungen (z.B. Zinsen) herauszugeben. Können Sie uns die emp-fangene Leistung sowie Nutzungen (z.B. Gebrauchsvorteile) nicht oder teilweise nicht oder nur in verschlechtertem Zustand zurückgewähren beziehungsweise herausgeben, müssen Sie uns insoweit Wertersatz leisten. Für die Verschlechterung der Sache und für gezogene Nutzungen müssen Sie Wertersatz nur leisten, soweit die Nutzungen oder die Verschlechterung auf einen Umgang mit der Sache zurückzuführen ist, der über die Prüfung der Eigenschaften und der Funktionsweise hinausgeht. Unter "Prüfung der Eigenschaften und der Funktionsweise" versteht man das Testen und Ausprobieren der jeweiligen Ware, wie es etwa im Ladengeschäft möglich und üblich ist. Paketversandfähige Sachen sind auf unsere Gefahr zurückzusenden. Sie haben die regelmäßigen Kosten der Rücksendung zu tragen, wenn die gelieferte Ware der bestellten entspricht und wenn der Preis der zurückzusendenden Sache einen Betrag von 40,- Euro nicht übersteigt oder wenn Sie bei einem höheren Preis der Sache zum Zeitpunkt des Widerrufs noch nicht die Gegenleistung oder eine vertraglich vereinbarte Teilzahlung erbracht haben. Anderenfalls ist die Rücksendung für Sie kostenfrei. Nicht paketversandfähige Sachen werden bei Ihnen abgeholt. Verpflichtungen zur Erstattung von Zahlungen müssen innerhalb von 30 Tagen erfüllt werden. Die Frist beginnt für Sie mit der Absendung Ihrer Widerrufserklärung oder der Sache, für uns mit deren Empfang. Ende der Widerrufsbelehrung</p>
  </div>
</section>

<footer>
  <nav class="nav nav-foot">
    <a href="#">Tovix-Shop</a><a href="#">Wir über Uns</a><a href="#">Rückgaberecht</a><a href="#">Versand</a><a href="#">Zahlung</a>
  </nav>
</footer>
</body>
</html>
```